One-page magazine ad for accountant serving the non-profit industry

I am Certified Public Accountant placing a one-page ad in Harvestlight Journal. The ad will be seen by churches and other non-profit organizations.
Harvestlight Journal requires the following:
Accepted file formats:
a) Press ready PDF with all fonts embedded. OR
b) Flattened CMYK Abode Photoshop PSD or illustrator PDF or EPS with all fonts outlined.
Ad Specs:
Trim 8" x 10.5"
Live 7.5" x 10"
Bleed 8.25" x 10.75"

I would like the ad to state the following information:

Marcus T. Velloway, CPA, CGMA

I am Certified Public Accountant with over 30 years of experience serving the accounting and tax needs of churches and non-profit organizations.

Some of the services I can offer:

Audits, Reviews, Compilations
Bookkeeping Services
Payroll Taxes
501C3 - IRS exemption applications
Clergy Housing Allowance issues and Personal Taxes

```html
<!DOCTYPE html>
<html lang="en">
<head>
<meta charset="utf-8">
<title>Marcus T. Velloway, CPA, CGMA</title>
<link rel="stylesheet" href="https://fonts.googleapis.com/css2?family=Arimo:wght@400;700&family=Lato:wght@400&display=swap">
<style>
  :root {
    --slate: #5a6675;
    --ink: #1b1d21;
    --white: #ffffff;
    --olive: #b3ad33;
  }
  * { margin: 0; padding: 0; box-sizing: border-box; }
  html, body { width: 921px; height: 1200px; overflow: hidden; background: var(--slate); }
  .ad {
    position: relative;
    width: 921px; height: 1200px;
    background: var(--slate);
    font-family: "Lato", "Gill Sans", sans-serif;
    color: var(--ink);
  }
  .headline {
    position: absolute; top: 58px; left: 0; width: 100%;
    text-align: center;
    font-family: "Arimo", Arial, sans-serif;
    font-weight: 700; font-size: 56px; line-height: 78px;
    color: var(--white);
    letter-spacing: 1px;
  }
  .headline-rule {
    position: absolute; top: 226px; left: 118px; width: 697px; height: 4px;
    background: var(--ink);
  }
  .intro {
    position: absolute; top: 274px; left: 110px; width: 700px;
    text-align: center; font-size: 31px; line-height: 49.5px;
  }
  .laurel-mark {
    position: absolute; left: 651px; top: 442px; width: 270px; height: 288px;
    border-radius: 50%;
    background: radial-gradient(circle, rgba(179,173,51,0.15) 35%, rgba(179,173,51,0.75) 62%, rgba(179,173,51,0) 72%);
  }
  .services-heading {
    position: absolute; top: 536px; left: 88px;
    font-family: "Arimo", Arial, sans-serif; font-weight: 700;
    font-size: 31px; line-height: 40px;
  }
  .services {
    position: absolute; top: 596px; left: 86px;
    list-style: none; font-size: 31px; line-height: 43.5px;
  }
  .services li::before { content: "\2022"; }
  .brand {
    position: absolute; left: 108px; top: 920px; width: 250px;
    text-align: center; color: var(--white);
  }
  .brand-name { font-size: 40px; line-height: 60px; margin-left: -42px; width: 250px; }
  .brand-rule { width: 128px; height: 3px; background: var(--white); margin: 30px 0 0 55px; }
  .brand-tagline {
    font-family: "Arimo", Arial, sans-serif;
    font-size: 25px; line-height: 34.5px; margin: 18px 0 0 -6px; width: 240px;
  }
  .divider {
    position: absolute; left: 404px; top: 927px; width: 3px; height: 217px;
    background: var(--ink);
  }
  .contact {
    position: absolute; left: 440px; top: 966px; width: 440px;
    text-align: center; color: var(--white);
    font-size: 25px; line-height: 37px;
  }
</style>
</head>
<body>
<main class="ad">
  <h1 class="headline">MARCUS T. VELLOWAY<br>CPA, CGMA</h1>
  <div class="headline-rule"></div>

  <p class="intro">I am a Certified Public Accountant with over 30 years of experience serving accounting and tax needs of churches and non-profit organizations.</p>

  <div class="laurel-mark" role="img" aria-label="Gold laurel wreath emblem surrounding balance scales"></div>

  <h2 class="services-heading">Some of the services I can offer:</h2>
  <ul class="services">
    <li>Audits, Reviews, Compilations</li>
    <li>Bookkeeping Services</li>
    <li>Payroll Taxes</li>
    <li>501C3 - IRS exemption applications</li>
    <li>Clergy Housing Allowance issues and Personal Taxes</li>
  </ul>

  <div class="brand">
    <div class="brand-name">Velloway</div>
    <div class="brand-rule"></div>
    <p class="brand-tagline">certified<br>public<br>accountant</p>
  </div>

  <div class="divider"></div>

  <address class="contact" style="font-style: normal;">
    Marcus T. Velloway, CPA, CGMA<br>
    email: marcus@vellowaycpa.com<br>
    telephone: (555) 214-0386
  </address>
</main>
</body>
</html>
```